business card letterhead envelope
Darren Holcomb Realtors
Project: business card letterhead envelope
business card letterhead envelope - Real Estate
Creative Brief
Professional
Darren Holcomb
Attorney/Broker
2817 W. Larkspur Ave Suite B7 Odessa, TX 79748
Darren@PecosPrairieHouses.com
PecosPrairieHouses.com

```html
<!DOCTYPE html>
<html lang="en">
<head>
<meta charset="utf-8">
<title>Darren Holcomb Realtors — Stationery</title>
<link href="https://fonts.googleapis.com/css2?family=Open+Sans:wght@400;600&display=swap" rel="stylesheet">
<style>
  :root {
    --backdrop: #878787;
    --paper: #ffffff;
    --ink: #2b2b2b;
    --band: #333333;
    --muted: #6d6d6d;
    --fold: #d9d9d9;
    --shadow: 0 2px 6px rgba(0,0,0,.35);
  }
  * { margin: 0; padding: 0; box-sizing: border-box; }
  html, body { width: 1200px; height: 684px; overflow: hidden; }
  body {
    background: var(--backdrop);
    font-family: "Open Sans", Arial, sans-serif;
    color: var(--ink);
    position: relative;
  }
  .sheet { position: absolute; background: var(--paper); box-shadow: var(--shadow); overflow: hidden; }

  .company-name {
    font-family: "Open Sans", Arial, sans-serif; font-weight: 400; color: var(--ink);
    text-align: center; white-space: nowrap; line-height: 1.2;
  }

  .band { position: absolute; left: 0; right: 0; background: var(--band); }
  .band-web { color: #fff; font-weight: 600; text-align: center; }
  .contact-line {
    position: absolute; left: 0; right: 0; text-align: center;
    color: var(--muted); white-space: nowrap;
  }

  /* letterhead */
  .letterhead { left: 187px; top: 31px; width: 432px; height: 643px; }
  .letterhead .band.top { top: 0; height: 8px; }
  .letterhead .company-name { position: absolute; top: 52px; left: 0; right: 0; font-size: 12px; }
  .letterhead .contact-line { top: 597px; font-size: 5.4px; }
  .letterhead .band.bottom { bottom: 0; height: 26px; display: flex; align-items: center; justify-content: center; font-size: 6px; }

  /* business card */
  .card { left: 101px; top: 312px; width: 199px; height: 110px; }
  .card .company-name { position: absolute; left: 6px; top: 42px; width: 88px; font-size: 7px; white-space: normal; }
  .card .details { position: absolute; left: 100px; top: 12px; font-size: 4.6px; line-height: 1.5; color: var(--muted); }
  .card .details .person { font-weight: 600; color: var(--ink); }
  .card .details .role { margin-bottom: 3px; }
  .card .band.bottom { bottom: 0; height: 16px; display: flex; align-items: center; justify-content: center; font-size: 5px; }

  /* envelope back */
  .envelope-back { left: 643px; top: 108px; width: 468px; height: 233px; }
  .envelope-back svg { position: absolute; inset: 0; }

  /* envelope front */
  .envelope-front { left: 643px; top: 367px; width: 468px; height: 223px; }
  .envelope-front .band.top { top: 0; height: 8px; }
  .envelope-front .company-name { position: absolute; top: 50px; left: 0; right: 0; font-size: 12px; }
  .envelope-front .contact-line { top: 164px; font-size: 5.4px; }
  .envelope-front .band.bottom { bottom: 0; height: 32px; display: flex; align-items: center; justify-content: center; font-size: 6px; }
</style>
</head>
<body>

  <section class="sheet letterhead" aria-label="Letterhead">
    <div class="band top"></div>
    <p class="company-name">Darren Holcomb Realtors</p>
    <p class="contact-line">2817 W. Larkspur Ave Suite B7 Odessa, TX 79748 &nbsp;|&nbsp; P: (432) 555-0147 &nbsp;|&nbsp; M: (432) 555-0162 &nbsp;|&nbsp; F: (432) 555-0148 &nbsp;|&nbsp; Darren@PecosPrairieHouses.com</p>
    <div class="band bottom band-web">www.PecosPrairieHouses.com</div>
  </section>

  <section class="sheet card" aria-label="Business card">
    <p class="company-name">Darren Holcomb Realtors</p>
    <div class="details">
      <p class="person">Darren Holcomb</p>
      <p class="role">Attorney/Broker</p>
      <p>P: (432) 555-0147</p>
      <p>M: (432) 555-0162</p>
      <p>F: (432) 555-0148</p>
      <p>Darren@PecosPrairieHouses.com</p>
      <p>2817 W. Larkspur Ave Suite B7</p>
      <p>Odessa, TX 79748</p>
    </div>
    <div class="band bottom band-web">www.PecosPrairieHouses.com</div>
  </section>

  <section class="sheet envelope-back" aria-label="Envelope back">
    <svg width="468" height="233" viewBox="0 0 468 233">
      <polyline points="0,2 234,96 468,2" fill="none" stroke="var(--fold)" stroke-width="1.2"/>
      <line x1="0" y1="233" x2="150" y2="120" stroke="var(--fold)" stroke-width="1"/>
      <line x1="468" y1="233" x2="318" y2="120" stroke="var(--fold)" stroke-width="1"/>
    </svg>
  </section>

  <section class="sheet envelope-front" aria-label="Envelope front">
    <div class="band top"></div>
    <p class="company-name">Darren Holcomb Realtors</p>
    <p class="contact-line">2817 W. Larkspur Ave Suite B7 Odessa, TX 79748 &nbsp;|&nbsp; P: (432) 555-0147 &nbsp;|&nbsp; M: (432) 555-0162 &nbsp;|&nbsp; F: (432) 555-0148 &nbsp;|&nbsp; Darren@PecosPrairieHouses.com</p>
    <div class="band bottom band-web">www.PecosPrairieHouses.com</div>
  </section>

</body>
</html>
```